Keelridge Ventures Consulting firm

I need a business card that is succint for a Brisbane based business called Keelridge Ventures Consulting Pty Ltd.
We bridge the gaps between People, Process and Technology.

We are a specialist operational excellence firm, delivering strategic consulting and business advisory services in six core capabilities, across all industries and all business lines to improve performance, efficiency, profitability, automation and scalability, for clients across Australia &New Zealand.
Updates

Hi Designers, I have uploaded the logo in 3D .png format, to assist in card design.

Target Market(s)

Project Management professionals, IT professionals, corporate and government clients managing transitioning or transformation projects.

Contact Information for Business Card

Keelridge Ventures Consulting Pty Ltd

Daniel Ostrava
Principal Consultant

mobile: +61 452 160 389
email: daniel@keelridgeventuresconsulting.com.au
webpage: www.keelridgeventuresconsulting.com

professional services: strategic advisors,

Font styles to use
Sans Serif

Requirements
Must have
• Business name: Keelridge Ventures Consulting
logo: attached
Contact person: Daniel Ostrava
Title: Principal Consultant
contact details:
mobile +61 452 160
email: daniel@KeelridgeVenturesConsulting.com.au
website: KeelridgeVenturesConsulting.com

on back side with logo include: A.B.N. 71482903165

professional services offered: Business Analysis, Strategic Advisory
Nice to have
• QR code
Should not have
• contacts picture

```html
<!DOCTYPE html>
<html lang="en">
<head>
<meta charset="utf-8">
<title>Keelridge Ventures Consulting – Business Card</title>
<link href="https://fonts.googleapis.com/css2?family=Poppins:wght@400;500;700&display=swap" rel="stylesheet">
<style>
  :root {
    --backdrop: #2b2b2e;
    --navy: #232a4d;
    --navy-soft: #2e365c;
    --red: #e3262a;
    --white: #ffffff;
    --silver: #c9ccd6;
    --ink: #232a4d;
  }
  * { box-sizing: border-box; margin: 0; padding: 0; }
  html, body { width: 1200px; height: 880px; overflow: hidden; }
  body {
    background: var(--backdrop);
    font-family: "Poppins", sans-serif;
    position: relative;
  }
  .card {
    position: absolute;
    left: 300px;
    width: 600px;
    height: 343px;
    border-radius: 22px;
    overflow: hidden;
    box-shadow: 0 14px 30px rgba(0,0,0,0.45);
  }
  .card--back { top: 80px; background: var(--navy); }
  .card--front { top: 457px; background: var(--white); }

  /* back */
  .world-map {
    position: absolute;
    left: 60px; top: 40px;
    width: 480px; height: 230px;
    border-radius: 40px;
    background: radial-gradient(ellipse at center, var(--navy-soft) 0%, var(--navy) 75%);
  }
  .back-brand {
    position: absolute;
    left: 0; right: 0; top: 82px;
    text-align: center;
    color: var(--silver);
    font-weight: 700;
    font-size: 40px;
    line-height: 1;
    letter-spacing: 1px;
  }
  .back-brand .brand-line { display: block; }
  .back-brand .brand-suffix { display: block; font-size: 11px; letter-spacing: 3px; margin-top: 8px; }
  .back-details {
    position: absolute;
    left: 0; right: 0; top: 222px;
    text-align: center;
    color: var(--white);
    font-size: 15px;
    line-height: 1.7;
    letter-spacing: 0.5px;
  }

  /* front */
  .front-band { position: absolute; inset: 0; }
  .front-brand {
    position: absolute;
    left: 32px; top: 46px;
    color: var(--white);
    font-weight: 700;
    font-size: 32px;
    line-height: 1.02;
  }
  .front-brand .brand-suffix { font-size: 10px; letter-spacing: 3px; display: block; margin-top: 6px; }
  .person {
    position: absolute;
    left: 40px; top: 222px;
  }
  .person-name { color: var(--ink); font-weight: 700; font-size: 20px; letter-spacing: 0.5px; line-height: 1.1; }
  .person-title { color: var(--red); font-weight: 500; font-size: 15px; line-height: 1.3; }
  .contacts { list-style: none; margin-top: 10px; }
  .contact {
    display: flex; align-items: center; gap: 9px;
    color: var(--ink);
    font-size: 13px;
    line-height: 20px;
  }
  .contact svg { width: 14px; height: 14px; flex: none; }
</style>
</head>
<body>

<section class="card card--back" aria-label="Card back">
  <div class="world-map" role="img" aria-label="Faint world map in the background"></div>
  <div class="back-brand">
    <span class="brand-line">KEELRIDGE</span>
    <span class="brand-line">VENTURES</span>
    <span class="brand-suffix">PTY LTD</span>
  </div>
  <div class="back-details">
    <p>A.B.N. 71482903165</p>
    <p>Business Analysis | Strategic Advisory</p>
  </div>
</section>

<section class="card card--front" aria-label="Card front">
  <svg class="front-band" width="600" height="343" viewBox="0 0 600 343" aria-hidden="true">
    <polygon points="0,0 540,0 0,205" fill="var(--navy)"/>
    <polygon points="0,205 540,0 572,0 0,218" fill="var(--red)"/>
  </svg>
  <div class="front-brand">
    KEELRIDGE<br>VENTURES
    <span class="brand-suffix">PTY LTD</span>
  </div>
  <div class="person">
    <p class="person-name">DANIEL OSTRAVA</p>
    <p class="person-title">Principal Consultant</p>
    <ul class="contacts">
      <li class="contact">
        <svg viewBox="0 0 14 14"><circle cx="7" cy="7" r="6.2" fill="none" stroke="var(--red)" stroke-width="1.4"/><rect x="5" y="3.5" width="4" height="7" rx="0.8" fill="var(--red)"/></svg>
        +61 452 160
      </li>
      <li class="contact">
        <svg viewBox="0 0 14 14"><circle cx="7" cy="7" r="6.2" fill="none" stroke="var(--red)" stroke-width="1.4"/><rect x="4" y="4.8" width="6" height="4.4" fill="var(--red)"/><polyline points="4,5 7,7.3 10,5" fill="none" stroke="var(--white)" stroke-width="0.8"/></svg>
        daniel@KeelridgeVenturesConsulting.com.au
      </li>
      <li class="contact">
        <svg viewBox="0 0 14 14"><circle cx="7" cy="7" r="6.2" fill="none" stroke="var(--red)" stroke-width="1.4"/><circle cx="7" cy="7" r="3.2" fill="none" stroke="var(--red)" stroke-width="1"/><line x1="3.8" y1="7" x2="10.2" y2="7" stroke="var(--red)" stroke-width="0.8"/><line x1="7" y1="3.8" x2="7" y2="10.2" stroke="var(--red)" stroke-width="0.8"/></svg>
        KeelridgeVenturesConsulting.com
      </li>
    </ul>
  </div>
</section>

</body>
</html>
```